Business Card Design Project - IT Company

CLOUD IT company working with medium to large corporate clients requires 2 sided Business Card design.

Strong, Professional and modern is what I am looking for.

The Logo JPG attached has all the colour palette options. which consist of Red and Silver on various backgrounds

Preferred option for the Back of card is either Silver Text on Red or Silver Text on Black. Though this is not concrete. Surprise me.

Logo must be prominent along with Contact details of the staff member

Tagline can be all Capitals " CLOUD MANAGED SERVICES"

I will look to provide feedback and tweaks to get the right design so it should be a fun process.

I will provide the layered files to the top few contenders.

Reason: Leaving the door open for some creativity. Don't forget this is an technology company. .

Target Market(s)

Leaders, decision makers, CEOs, CIOs,

Industry/Entity Type

Business

Requirements
Must have
• Data must have is

Company Name: Velquora
Tagline: Cloud Managed Services

No Particular order

First Name Last name
Director
Mobile 0452 987 654
www.velquora.com
First.Lastname@velquora.com
Suite 5, 48 Marlowe Lane, Sydney NSW 2000

```html
<!DOCTYPE html>
<html lang="en">
<head>
<meta charset="utf-8">
<title>Velquora Business Card</title>
<link rel="stylesheet" href="https://fonts.googleapis.com/css2?family=Arimo:ital,wght@0,400;0,700;1,400&display=swap">
<style>
  :root {
    --card-red: #a61d29;
    --panel-red: #9c1f27;
    --ink-white: #ffffff;
    --ink-black: #111111;
    --silver: #cfcfd1;
    --emblem-grey: #6f6f6f;
  }
  html, body {
    margin: 0;
    padding: 0;
    overflow: hidden;
  }
  .card {
    position: relative;
    width: 1200px;
    height: 1000px;
    background: var(--card-red);
    overflow: hidden;
    font-family: "Arimo", Arial, sans-serif;
    color: var(--ink-white);
  }
  .connectors {
    position: absolute;
    left: 0;
    top: 0;
  }
  .emblem {
    position: absolute;
    left: 236px;
    top: 778px;
    width: 124px;
    height: 124px;
  }
  .info {
    position: absolute;
    margin: 0;
    font-style: italic;
    font-weight: 400;
    line-height: 1.3;
    white-space: nowrap;
  }
  .address { left: 92px; top: 111px; width: 400px; text-align: center; font-size: 20px; }
  .website { left: 104px; top: 243px; font-size: 21px; }
  .email { left: 346px; top: 228px; font-size: 20.5px; }
  .mobile { left: 98px; top: 374px; width: 400px; text-align: center; font-size: 26px; }
  .person-name { left: 104px; top: 426px; font-size: 26px; line-height: 1.2; }
  .person-title { left: 394px; top: 431px; font-size: 25.5px; }
  .company-name { left: 102px; top: 588px; width: 400px; text-align: center; font-size: 41px; }

  .logo-panel {
    position: absolute;
    left: 783px;
    top: 178px;
    width: 244px;
    height: 645px;
    background: var(--panel-red);
  }
  .logo-lockup {
    position: absolute;
    left: 585px;
    top: 400px;
    width: 640px;
    height: 200px;
    transform: rotate(-90deg);
    display: flex;
    align-items: center;
    gap: 28px;
    color: var(--silver);
  }
  .logo-dot {
    flex: none;
    width: 100px;
    height: 100px;
    border-radius: 50%;
    background: var(--silver);
  }
  .logo-words {
    display: flex;
    flex-direction: column;
  }
  .logo-name {
    font-weight: 700;
    font-size: 100px;
    line-height: 1;
  }
  .logo-tagline {
    font-weight: 700;
    font-size: 25px;
    letter-spacing: 0.5px;
    line-height: 1.2;
    margin-top: 6px;
  }
</style>
</head>
<body>
<main class="card">
  <svg class="connectors" width="1200" height="1000" viewBox="0 0 1200 1000" aria-hidden="true">
    <g stroke="var(--ink-black)" stroke-width="5" stroke-dasharray="8 6" fill="none">
      <line x1="298" y1="222" x2="298" y2="312"/>
      <line x1="208" y1="300" x2="275" y2="366"/>
      <line x1="385" y1="300" x2="318" y2="367"/>
      <line x1="298" y1="436" x2="298" y2="526"/>
      <line x1="211" y1="509" x2="277" y2="574"/>
      <line x1="386" y1="510" x2="322" y2="574"/>
      <line x1="298" y1="660" x2="298" y2="750"/>
    </g>
  </svg>

  <svg class="emblem" viewBox="0 0 124 124" role="img" aria-label="Round home emblem">
    <circle cx="62" cy="62" r="62" fill="var(--emblem-grey)"/>
  </svg>

  <p class="info address">Suite 5, 48 Marlowe Lane,<br>Sydney NSW 2000</p>
  <p class="info website">www.velquora.com</p>
  <p class="info email">First.Lastname<br>@velquora.com</p>
  <p class="info mobile">Mobile 0452 987 654</p>
  <p class="info person-name">First Name<br>Last name</p>
  <p class="info person-title">Director</p>
  <p class="info company-name">Velquora</p>

  <div class="logo-panel"></div>
  <div class="logo-lockup">
    <span class="logo-dot"></span>
    <div class="logo-words">
      <span class="logo-name">Velquora</span>
      <span class="logo-tagline">CLOUD MANAGED SERVICES</span>
    </div>
  </div>
</main>
</body>
</html>
```